www.propulsezvoscommerces.ca

J'ai besoin d'un flyer design pour mon entreprise de consultant - coach
que vous avez déjà produit pour moi (page web). À partir de ma page web concevoir un flyer. Vous remarquerez j'ai ajouter 3 pages:
Conférence + Formation + Motivation
Donc élaborer un flyer
Merci
Lucien Morvan
Consultant - Coach

Gens d'affaires : Concessionnaire Auto, Constructeur Immobilier

Consultant

Serif

```html
<!DOCTYPE html>
<html lang="fr">
<head>
<meta charset="utf-8">
<title>Lucien Morvan – Consultant Coach</title>
<link rel="stylesheet" href="https://fonts.googleapis.com/css2?family=Cinzel:wght@600&family=Roboto:wght@400;700;900&family=Roboto+Condensed:wght@700&family=Playfair+Display:ital@1&display=swap">
<style>
  :root {
    --cream: #f3e7e3;
    --panel: #f0e1dc;
    --slate: #6f6d6c;
    --slate-dark: #4f4e4d;
    --ink: #4a4a4a;
    --ink-soft: #5c5c5c;
    --orange: #e98a2c;
    --gold-light: #f4d98c;
    --gold: #caa047;
    --gold-dark: #9b7426;
    --white: #ffffff;
    --photo-a: #8a6a5c;
    --photo-b: #3b3836;
  }
  * { margin: 0; padding: 0; box-sizing: border-box; }
  html, body { width: 849px; height: 1200px; overflow: hidden; }
  body { font-family: "Roboto", Arial, sans-serif; }

  .flyer {
    position: relative;
    width: 849px;
    height: 1200px;
    background: linear-gradient(180deg, var(--slate) 0%, var(--slate-dark) 100%);
    overflow: hidden;
  }

  .hero {
    position: absolute;
    left: 0; top: 0;
    width: 849px; height: 465px;
    background: var(--cream);
  }

  .portrait {
    position: absolute;
    left: 0; top: 0;
    width: 345px; height: 400px;
    background: radial-gradient(ellipse at 55% 40%, var(--photo-a) 0%, #6a5148 45%, var(--photo-b) 100%);
  }

  .brand {
    position: absolute;
    left: 385px; top: 26px;
    width: 400px;
    display: flex;
    align-items: center;
    gap: 14px;
  }
  .brand-mark {
    width: 54px; height: 54px;
    border-radius: 50%;
    background: var(--ink);
    flex: none;
  }
  .brand-text { display: flex; flex-direction: column; }
  .brand-name {
    font-family: "Cinzel", Georgia, serif;
    font-weight: 600;
    font-size: 38px;
    line-height: 1;
    color: var(--ink);
  }
  .brand-role {
    font-family: "Cinzel", Georgia, serif;
    font-size: 11px;
    letter-spacing: 3px;
    color: var(--ink-soft);
    margin-top: 4px;
    margin-left: 40px;
  }
  .brand-tagline {
    font-family: "Playfair Display", Georgia, serif;
    font-style: italic;
    font-size: 19px;
    color: var(--ink);
    margin-left: 40px;
    letter-spacing: 1px;
  }

  .headline {
    position: absolute;
    left: 345px; top: 160px;
    width: 490px;
    text-align: center;
    font-family: "Roboto Condensed", Arial, sans-serif;
    font-weight: 700;
  }
  .headline-kicker { font-size: 32px; color: var(--orange); line-height: 1.1; }
  .headline-main { font-size: 54px; color: var(--orange); line-height: 1.05; margin-top: 6px; }
  .headline-sub { font-size: 39px; color: var(--orange); line-height: 1.1; }

  .pitch {
    position: absolute;
    left: 345px; top: 322px;
    width: 490px;
    text-align: center;
    font-size: 15.5px;
    font-weight: 700;
    color: var(--ink);
    line-height: 1.4;
  }
  .pitch-close {
    position: absolute;
    left: 345px; top: 412px;
    width: 490px;
    text-align: center;
    font-family: "Roboto Condensed", Arial, sans-serif;
    font-weight: 700;
    font-size: 34px;
    color: var(--ink);
  }

  .service {
    position: absolute;
    left: 34px;
    width: 781px;
    height: 160px;
    background: var(--panel);
    padding: 16px 18px;
  }
  .service-title {
    font-family: "Roboto", Arial, sans-serif;
    font-weight: 700;
    font-size: 31px;
    color: var(--white);
    text-shadow: 0 0 2px rgba(0,0,0,0.15);
  }
  .service--conference { top: 487px; }
  .service--formation  { top: 656px; }
  .service--motivation { top: 825px; }

  .phone-bar {
    position: absolute;
    left: 176px; top: 998px;
    width: 498px; height: 86px;
    border-radius: 4px;
    background: linear-gradient(180deg, var(--gold-light) 0%, var(--gold) 50%, var(--gold-dark) 100%);
    box-shadow: 0 2px 6px rgba(0,0,0,0.35);
    display: flex; align-items: center; justify-content: center;
    font-family: "Roboto", Arial, sans-serif;
    font-weight: 900;
    font-size: 56px;
    color: var(--white);
    text-shadow: 0 2px 3px rgba(0,0,0,0.4);
  }

  .contact-email {
    position: absolute;
    left: 0; top: 1100px;
    width: 849px;
    text-align: center;
    font-family: "Roboto Condensed", Arial, sans-serif;
    font-size: 28px;
    color: var(--white);
  }
  .contact-web {
    position: absolute;
    left: 0; top: 1144px;
    width: 849px;
    text-align: center;
    font-size: 30px;
    letter-spacing: 7px;
    color: var(--white);
  }
</style>
</head>
<body>
<main class="flyer">
  <section class="hero">
    <div class="portrait" role="img" aria-label="Portrait photo of Lucien Morvan, consultant and coach, in a dark suit"></div>

    <div class="brand">
      <div class="brand-mark"></div>
      <div class="brand-text">
        <span class="brand-name">LUCIEN MORVAN</span>
        <span class="brand-role">CONSULTANT – COACH</span>
        <span class="brand-tagline">Devenir la référence!</span>
      </div>
    </div>

    <div class="headline">
      <p class="headline-kicker">DEVENIR LA RÉFÉRENCE!</p>
      <p class="headline-main">L'OBJECTIF:</p>
      <p class="headline-sub">AUGMENTEZ LES VENTES!</p>
    </div>

    <p class="pitch">
      Le meilleur investissement : votre personnel des ventes.<br>
      L'univers des ventes changent : innover et se réinventer.<br>
      Votre source de motivation est l'ingrédient qui peut faire:
    </p>
    <p class="pitch-close">TOUTE LA DIFFÉRENCE</p>
  </section>

  <section class="service service--conference"><h2 class="service-title">CONFERENCE</h2></section>
  <section class="service service--formation"><h2 class="service-title">FORMATION</h2></section>
  <section class="service service--motivation"><h2 class="service-title">MOTIVATION</h2></section>

  <div class="phone-bar">(819) 555-0142</div>
  <p class="contact-email">info@propulsezvoscommerces.ca</p>
  <p class="contact-web">www.propulsezvoscommerces.ca</p>
</main>
</body>
</html>
```